Modern, cutting edge crypto trading website.

I need a single-page website design, approximate 4-5 pages. I have included a screenshot of the inside of the current application for some reference for what it currently looks like. This is the public side of the application for not logged in users.

I am currently thinking about 3-5 sections of the page.
Menu at top is optional, these could be the sections of the site.
1. Above the fold cool, grabbing stuff.
2. What problem does this solve
3. Additional benefits
4. Pricing
5. Open to ideas! Well it's all open to ideas if you have ideas.

I am nervous about hiring designers, I am open to a further discussion for more work for additional money but I have to LIKE your design. So this could be considered a trial. I would like to continue to design the application itself and match everything together!

I really like the tradewisp website.

Competitor websites:
https://7ridges.example/
https://www.tradewisp.example/

Target Market(s)

Adults 25-50 mostly male,

Number of Pages Required

4 page

Colors

Designer to choose colors to be used in the design.

Requirements
Must have
• Modern design, clean lines, professional.
Nice to have
• Fun SVG stuff. Not for this price, but in the future.
Should not have
• Should not be cluttered OR too spacey. Quince's website has too much open space sometimes.

```html
<!DOCTYPE html>
<html lang="en">
<head>
<meta charset="utf-8">
<title>Signalwell — Crypto Trading Business</title>
<link href="https://fonts.googleapis.com/css2?family=Montserrat:wght@500;600;700&family=Source+Sans+3:wght@400;600;700&display=swap" rel="stylesheet">
<style>
:root{
  --navy:#14348c;
  --navy-deep:#0b2470;
  --blue:#3d7ee0;
  --ink:#1b1d2a;
  --text:#5a5d66;
  --muted:#8b8e96;
  --line:#e0e0e4;
  --footer-bar:#0c0d11;
  --nav-light:#dfe8ff;
  --white:#fff;
}
*{box-sizing:border-box;margin:0;padding:0}
html,body{width:1200px;height:4133px;overflow:hidden}
body{position:relative;background:var(--white);font-family:"Source Sans 3",sans-serif;color:var(--text)}
.abs{position:absolute}
.head{font-family:"Montserrat",sans-serif;color:var(--ink)}
.btn{position:absolute;display:flex;align-items:center;justify-content:center;border-radius:26px;background:linear-gradient(180deg,var(--navy),var(--navy-deep));color:var(--white);font-family:"Montserrat",sans-serif;font-weight:700;font-size:16px;letter-spacing:.3px;box-shadow:0 6px 14px rgba(20,52,140,.25)}
.rule{position:absolute;width:20px;height:4px;background:var(--navy)}

/* hero artwork sits beneath the header */
.hero-art{right:0;top:0;z-index:0}

/* header */
.brand{left:90px;top:28px;z-index:2;display:flex;align-items:center;gap:10px;font-family:"Montserrat",sans-serif;font-weight:700;font-size:20px;letter-spacing:1.5px;color:var(--ink)}
.brand-mark{width:34px;height:30px;background:var(--navy)}
.nav{left:399px;top:37px;z-index:2;display:flex;gap:26px;font-size:15px;color:var(--ink)}
.nav .on{color:var(--navy);font-weight:600;border-bottom:2px solid var(--navy)}
.nav .over{color:var(--nav-light)}
.login{left:1003px;top:26px;width:105px;height:41px;font-size:15px;z-index:2}

/* hero */
.hero-title{left:90px;top:196px;font-size:36px;font-weight:700;letter-spacing:.5px;z-index:1}
.hero-sub{left:90px;top:238px;font-family:"Montserrat",sans-serif;font-size:37px;font-weight:600;color:var(--blue);z-index:1}
.hero-copy{left:90px;top:305px;width:455px;font-size:16.5px;line-height:30.5px;text-align:justify;z-index:1}
.start{left:90px;top:460px;width:196px;height:48px}

.partners{left:90px;top:715px;width:1020px;display:flex;justify-content:space-between;align-items:center;font-family:"Montserrat",sans-serif;font-size:17px;font-weight:600;color:#8d8f96}

/* problem */
.problem-art{left:-60px;top:812px;width:650px;height:525px;border-radius:50%;background:radial-gradient(circle at 55% 50%,#3a5fd0 0,#2b47b8 22%,#f3f3f5 42%,#f3f3f5 100%)}
.problem-title{left:634px;top:840px;font-size:31px;font-weight:600;line-height:40px}
.problem-copy{left:634px;top:983px;width:482px;font-size:16px;line-height:34px;text-align:justify}
.read{left:634px;top:1177px;width:160px;height:50px}

/* strategy band */
.band{left:0;top:1410px}
.strat-title{left:90px;top:1566px;font-size:32px;font-weight:600;color:var(--white)}
.strat-copy{left:90px;top:1665px;width:480px;font-size:16px;line-height:29.5px;color:#e4eaf8}
.outline{position:absolute;left:90px;top:1797px;width:161px;height:50px;border:2px solid var(--white);border-radius:26px;display:flex;align-items:center;justify-content:center;color:var(--white);font-family:"Montserrat",sans-serif;font-weight:700;font-size:16px}
.laptop{left:654px;top:1493px;width:546px;height:460px;background:var(--white);border-radius:14px 0 0 0;padding:26px 0 0 22px}
.screen{width:100%;height:100%;background:linear-gradient(90deg,#2a2b2f 0 18%,#f5f5f6 18% 100%)}
.laptop-base{left:585px;top:1953px;width:615px;height:15px;background:linear-gradient(180deg,#e5e6ea,#b9bcc4);border-radius:0 0 0 40px}

/* benefits */
.center-title{position:absolute;left:0;width:1200px;text-align:center;font-size:32px;font-weight:600}
.benefit{position:absolute;top:2239px;width:290px}
.benefit-icon{width:57px;height:52px;background:var(--navy);border-radius:3px;display:flex;align-items:center;justify-content:center}
.benefit h3{margin-top:22px;font-family:"Montserrat",sans-serif;font-weight:500;font-size:18px;color:var(--ink)}
.benefit p{margin-top:12px;font-size:15px;line-height:27px;white-space:nowrap}

/* pricing */
.pricing-bg{left:0;top:2540px}
.card{position:absolute;top:2810px;width:286px;height:318px;background:var(--white);box-shadow:0 4px 18px rgba(0,0,0,.05)}
.price{position:absolute;left:50%;top:-54px;width:106px;height:106px;margin-left:-53px;border-radius:50%;background:var(--white);box-shadow:0 2px 10px rgba(0,0,0,.08);display:flex;align-items:center;justify-content:center;font-size:28px;color:var(--navy)}
.price small{font-size:15px;margin-top:10px}
.plan{position:absolute;top:64px;width:100%;text-align:center;font-family:"Montserrat",sans-serif;font-size:23px;font-weight:500;color:var(--navy)}
.features{position:absolute;top:106px;left:28px;right:28px;list-style:none}
.features li{height:45px;line-height:45px;text-align:center;font-size:16px;color:var(--muted);border-top:1px dashed var(--line)}
.features li:last-child{border-bottom:1px dashed var(--line)}
.buy{left:50%;margin-left:-74px;top:295px;width:148px;height:49px}

/* stats */
.stats{left:148px;top:3398px;width:908px;display:flex}
.stat{flex:1;text-align:center;border-right:1px solid var(--line);height:140px;padding-top:14px}
.stat:last-child{border-right:none}
.stat b{display:block;margin-top:26px;font-family:"Montserrat",sans-serif;font-size:18px;color:var(--navy)}
.stat span{display:block;margin-top:6px;font-size:15px;color:var(--text)}

/* footer */
.footer{left:0;top:3660px}
.f-head{position:absolute;top:3775px;font-family:"Montserrat",sans-serif;font-size:27px;font-weight:500;color:var(--white)}
.f-list{position:absolute;top:3828px;left:90px;list-style:none;font-size:13px;line-height:27px;color:#d8d9de}
.f-text{position:absolute;font-size:13px;line-height:28px;color:#d8d9de;white-space:nowrap}
.signup{left:563px;top:3868px;width:279px;height:38px;border:2px solid var(--white);border-radius:20px;background:var(--white);display:flex;align-items:center;justify-content:space-between;padding:0 3px 0 14px;font-size:12px;color:#9a9ca3}
.signup b{background:var(--navy);color:var(--white);font-weight:600;font-size:13px;border-radius:16px;padding:6px 14px}
.socials{left:567px;top:3958px;display:flex;gap:22px}
.socials i{width:14px;height:14px;border-radius:50%;background:#e9eaee;display:block}
.socials i.on{background:#2f8fe0}
.signin{left:919px;top:3784px;width:189px;height:50px;background:var(--white);color:var(--navy);box-shadow:none}
.create{left:919px;top:3845px;width:189px;height:49px}
.copy{left:0;top:4080px;width:1200px;height:53px;background:var(--footer-bar);text-align:center;line-height:53px;font-size:12px;color:#c9cad0}
</style>
</head>
<body>

<!-- hero artwork -->
<svg class="abs hero-art" width="650" height="660" viewBox="0 0 650 660" role="img" aria-label="Isometric illustration of a blue crypto city with trading screens and towers">
  <defs>
    <linearGradient id="heroBlob" x1="0" y1="0" x2="1" y2="1">
      <stop offset="0" stop-color="#3f6fe6"/><stop offset=".55" stop-color="#1d36a6"/><stop offset="1" stop-color="#2a5be0"/>
    </linearGradient>
  </defs>
  <path d="M300 0H650V610C560 660 420 665 310 620 180 568 70 540 20 430-20 340 40 250 110 200 200 140 260 80 300 0Z" fill="url(#heroBlob)"/>
</svg>

<!-- header -->
<div class="abs brand"><span class="brand-mark"></span>SIGNALWELL</div>
<nav class="abs nav">
  <span class="on">HOME</span><span>ABOUT US</span><span>SOLUTION</span><span>BENEFITS</span><span>PRICING</span><span class="over">BLOG</span><span class="over">CONTACT US</span>
</nav>
<div class="btn login">LOGIN</div>

<!-- hero -->
<h1 class="abs head hero-title">SIGNALWELL</h1>
<div class="abs hero-sub">Crypto Trading Business</div>
<p class="abs hero-copy">Lorem ipsum dolor sit amet, consectetur ing elit, sed do mod tempor incididunt ut labore et dolore magna aliqua. Ut enim ad minim veniam, quis nostrud exercitation ullamco laboris nisi ut aliquip ex ea commodo consequat.</p>
<div class="btn start">GET STARTED</div>

<div class="abs partners">
  <span>LUMEN ATELIER</span><span>CARDMINT</span><span>PLACEHOLDER LABS</span><span>GLAD CLIENT</span><span>VERSANTO</span>
</div>

<!-- problem -->
<div class="abs problem-art" role="img" aria-label="Isometric illustration of a crypto trading platform with charts and coins"></div>
<h2 class="abs head problem-title">What problem does<br>this solve ?</h2>
<div class="rule" style="left:634px;top:943px"></div>
<p class="abs problem-copy">Lorem ipsum dolor sit amet, consectetur adipiscing elit, sed do eiusmod tempor incididunt ut labore et dolore magna aliqua. Ut enim ad minim veniam, quis nostrud exercitation ullamco laboris nisi ut aliquip ex ea commodo consequat. Duis aute irure dolor in reprehenderit in voluptate velit esse cillum dolore eu fugiat nulla pariatur.</p>
<div class="btn read">READ MORE</div>

<!-- strategy band -->
<svg class="abs band" width="1200" height="650" viewBox="0 0 1200 650" aria-hidden="true">
  <defs>
    <linearGradient id="bandFill" x1="0" y1="0" x2="0" y2="1">
      <stop offset="0" stop-color="#17328a"/><stop offset="1" stop-color="#0d55b3"/>
    </linearGradient>
  </defs>
  <path d="M0 10C300 50 700 60 1200 0V610C900 660 400 640 0 595Z" fill="url(#bandFill)"/>
</svg>
<h2 class="abs head strat-title">Strategy New</h2>
<div class="rule" style="left:90px;top:1626px;background:#fff"></div>
<p class="abs strat-copy">Lorem ipsum dolor sit amet, consectetur adipiscing elit, sed do eiusmod tempor incididunt ut labore et dolore magna aliqua. Ut enim ad minim veniam, quis nostrud exercitation ullamco laboris nisi ut aliquip ex ea</p>
<div class="outline">READ MORE</div>
<div class="abs laptop"><div class="screen" role="img" aria-label="Screenshot of the strategies dashboard inside the application"></div></div>
<div class="abs laptop-base"></div>

<!-- benefits -->
<h2 class="center-title head" style="top:2120px">Benefits</h2>
<div class="rule" style="left:590px;top:2181px"></div>
<div class="benefit" style="left:88px">
  <div class="benefit-icon"><svg width="32" height="32" viewBox="0 0 32 32" fill="none" stroke="#fff" stroke-width="1.6"><circle cx="16" cy="16" r="4"/><path d="M16 2v8M16 22v8M2 16h8M22 16h8M6 6l6 6M20 20l6 6M26 6l-6 6M12 20l-6 6"/></svg></div>
  <h3>Lorem ipsum dolor</h3>
  <p>Lorem ipsum dolor sit amet, consectetur<br>adipiscing elit, sed do eiusmod tempor<br>Lorem ipsum dolor sit amet</p>
</div>
<div class="benefit" style="left:470px">
  <div class="benefit-icon"><svg width="32" height="32" viewBox="0 0 32 32" fill="none" stroke="#fff" stroke-width="1.6"><circle cx="16" cy="17" r="9"/><path d="M16 12v10M4 4h6M22 4h6"/></svg></div>
  <h3>Lorem ipsum dolor</h3>
  <p>Lorem ipsum dolor sit amet, consectetur<br>adipiscing elit, sed do eiusmod tempor<br>Lorem ipsum dolor sit amet</p>
</div>
<div class="benefit" style="left:852px">
  <div class="benefit-icon"><svg width="32" height="32" viewBox="0 0 32 32" fill="none" stroke="#fff" stroke-width="1.6"><rect x="4" y="9" width="24" height="16" rx="2"/><path d="M8 20l5-5 4 3 7-6M20 5h6v4"/></svg></div>
  <h3>Lorem ipsum dolor</h3>
  <p>Lorem ipsum dolor sit amet, consectetur<br>adipiscing elit, sed do eiusmod tempor<br>Lorem ipsum dolor sit amet</p>
</div>

<!-- pricing -->
<svg class="abs pricing-bg" width="1200" height="730" viewBox="0 0 1200 730" aria-hidden="true">
  <path d="M0 70C150 40 260 90 420 60 600 25 720 20 860 50 1000 80 1100 55 1200 45V680C1050 700 950 640 780 660 600 680 500 640 300 650 150 660 60 700 0 700Z" fill="#efeff1"/>
  <path d="M0 65C180 20 300 70 470 45 650 15 760 40 900 35 1050 30 1120 60 1200 40" fill="none" stroke="#e4e4e7" stroke-width="14"/>
</svg>
<h2 class="center-title head" style="top:2672px">Pricing</h2>
<div class="rule" style="left:590px;top:2734px"></div>

<div class="card" style="left:148px">
  <div class="price">$99/<small>mn</small></div>
  <div class="plan">Basic</div>
  <ul class="features"><li>Lorem ipsum dolor sit amet</li><li>Lorem ipsum dolor sit amet</li><li>Lorem ipsum dolor sit amet</li></ul>
  <div class="btn buy">BUY NOW</div>
</div>
<div class="card" style="left:457px">
  <div class="price">$129/<small>mn</small></div>
  <div class="plan">Standard</div>
  <ul class="features"><li>Lorem ipsum dolor sit amet</li><li>Lorem ipsum dolor sit amet</li><li>Lorem ipsum dolor sit amet</li></ul>
  <div class="btn buy">BUY NOW</div>
</div>
<div class="card" style="left:767px">
  <div class="price">$288/<small>mn</small></div>
  <div class="plan">Premium</div>
  <ul class="features"><li>Lorem ipsum dolor sit amet</li><li>Lorem ipsum dolor sit amet</li><li>Lorem ipsum dolor sit amet</li></ul>
  <div class="btn buy">BUY NOW</div>
</div>

<!-- stats -->
<div class="abs stats">
  <div class="stat"><svg width="34" height="30" viewBox="0 0 34 30" fill="none" stroke="#14348c" stroke-width="1.6"><path d="M3 28h28M7 27V18M13 27V14M19 27V16M25 27V9M5 12l8-6 6 4 10-7"/></svg><b>50M+</b><span>Trading Volume (USD)</span></div>
  <div class="stat"><svg width="34" height="30" viewBox="0 0 34 30" fill="none" stroke="#14348c" stroke-width="1.6"><circle cx="17" cy="15" r="7"/><path d="M17 3v4M17 23v4M5 15h4M25 15h4"/></svg><b>300K</b><span>Transactions</span></div>
  <div class="stat"><svg width="34" height="30" viewBox="0 0 34 30" fill="none" stroke="#14348c" stroke-width="1.6"><rect x="5" y="3" width="18" height="22"/><path d="M9 9h10M9 14h6"/><circle cx="24" cy="21" r="5"/></svg><b>40K+</b><span>Happy Users</span></div>
  <div class="stat"><svg width="34" height="30" viewBox="0 0 34 30" fill="none" stroke="#14348c" stroke-width="1.6"><rect x="6" y="3" width="20" height="24"/><path d="M10 17l4-4 3 3 5-6M10 22h12"/></svg><b>10K+</b><span>Custom Portfolios Created</span></div>
</div>

<!-- footer -->
<svg class="abs footer" width="1200" height="473" viewBox="0 0 1200 473" aria-hidden="true">
  <path d="M0 0C300 40 800 45 1200 10V473H0Z" fill="#15161c"/>
</svg>
<h3 class="f-head" style="left:90px">Links</h3>
<ul class="f-list"><li>Home</li><li>About Us</li><li>Solution</li><li>Benefits</li><li>Pricing</li><li>Blog</li><li>Contact Us</li></ul>
<h3 class="f-head" style="left:262px">Contact Us</h3>
<p class="f-text" style="left:264px;top:3824px">At vero eos et accusamus 4B Marrow Lane, OR 97000<br>Ph: 555-010-4821<br>hello@signalwell.example</p>
<h3 class="f-head" style="left:562px">Newsletter</h3>
<p class="f-text" style="left:562px;top:3824px">Subscribe Our Newsletter For More Info</p>
<div class="abs signup">Email Address<b>SUBSCRIBE</b></div>
<div class="abs socials" role="img" aria-label="Social media links"><i></i><i></i><i class="on"></i><i></i></div>
<div class="btn signin">SIGN IN</div>
<div class="btn create">CREATE ACCOUNT</div>
<div class="abs copy">© 2019 Copyrights.The Company Name.All Rights Reserved</div>

</body>
</html>
```